Filmproduktion braucht Visitenkarten und Briefpapier
Zielgruppe
Wir sind eine junge Filmproduktion Firma mit dem Namen Kolbenhain.
Unser Kerngeschäft sind Image und Unternehmensfilme, sowie Event und Messefilme.
Aufgabenstellung
Wir sind junge, kreative, Filmschaffende und das soll sich auch in der Visitenkarte widerspiegeln, dennoch macht bitte auch ein paar klassische Vorschläge, manchmal ist weniger mehr.
Unser altes Briefpapier ist angehängt. Das neue Briefpapier muss von uns veränderbar sein, da wir noch nicht alle Daten haben wie Steuernummer und USt-ID, bitte aber schon als Dummy anlegen.
Unsere alten Visitenkarten sind angehängt, diese Daten Stimmen, aber ansonsten stimmt daran nix, wie wir finden. Bitte nicht daran Orientieren!!!
Bitte bei der Adresse Kolbenhain GbR schreiben.
Unser neues Logo, jetzt in blau ist ebenfalls angehängt.
Viel Spass beim Designen.

```html
<!DOCTYPE html>
<html lang="de">
<head>
<meta charset="utf-8">
<title>Kolbenhain – Visitenkarten</title>
<link rel="stylesheet" href="https://fonts.googleapis.com/css2?family=Fira+Sans+Condensed:wght@300;400;600&display=swap">
<style>
  :root {
    --bg: #e4e5e6;
    --paper: #f1f1f1;
    --blue-light: #6aa9d6;
    --blue-mid: #4f8fc4;
    --blue-dark: #3a74ab;
    --ink: #2b2b2b;
    --white: #ffffff;
    --shadow: rgba(0, 0, 0, 0.18);
  }
  * { margin: 0; padding: 0; box-sizing: border-box; }
  html, body {
    width: 1200px;
    height: 880px;
    overflow: hidden;
    background: var(--bg);
    font-family: "Fira Sans Condensed", sans-serif;
  }
  .canvas {
    width: 1200px;
    height: 880px;
    display: flex;
    align-items: center;
    justify-content: center;
    gap: 44px;
  }
  .card {
    width: 520px;
    height: 336px;
    position: relative;
    overflow: hidden;
    box-shadow: 0 10px 26px var(--shadow);
  }

  /* Vorderseite */
  .card-front { background: var(--paper); }
  .card-front .brand-area {
    height: 62%;
    display: flex;
    flex-direction: column;
    align-items: center;
    justify-content: center;
    gap: 18px;
  }
  .brand-dot {
    width: 46px;
    height: 46px;
    border-radius: 50%;
    background: var(--blue-mid);
  }
  .wordmark {
    font-weight: 300;
    font-size: 22px;
    letter-spacing: 0.55em;
    padding-left: 0.55em;
    text-transform: uppercase;
  }
  .card-front .wordmark { color: var(--ink); }
  .contact-band {
    position: absolute;
    left: 0; right: 0; bottom: 0;
    height: 38%;
    background: linear-gradient(90deg, var(--blue-light), var(--blue-mid));
    color: var(--white);
    padding: 22px 30px 0 150px;
    font-size: 14.5px;
    font-weight: 300;
    line-height: 1.55;
  }
  .contact-band .company { font-weight: 600; }

  /* Rückseite */
  .card-back {
    background: linear-gradient(135deg, var(--blue-light) 0%, var(--blue-mid) 50%, var(--blue-dark) 100%);
    display: flex;
    flex-direction: column;
    align-items: center;
    justify-content: center;
    gap: 24px;
  }
  .card-back .brand-dot { background: var(--white); width: 58px; height: 58px; }
  .card-back .wordmark { color: var(--white); font-size: 26px; }
</style>
</head>
<body>
<main class="canvas">
  <section class="card card-front" aria-label="Visitenkarte Vorderseite">
    <div class="brand-area">
      <span class="brand-dot"></span>
      <span class="wordmark">Kolbenhain</span>
    </div>
    <div class="contact-band">
      <p>Jonas Beispielmann | Geschäftsführer</p>
      <p><span class="company">Kolbenhain</span> | Filmproduktion | Lindenweg 4 | 10115 Berlin</p>
      <p>mail@kolbenhain.de | www.kolbenhain.de | 01234 / 56789-0</p>
    </div>
  </section>

  <section class="card card-back" aria-label="Visitenkarte Rückseite">
    <span class="brand-dot"></span>
    <span class="wordmark">Kolbenhain</span>
  </section>
</main>
</body>
</html>
```